Business Card & Full Stationary design For Summit Quarry
Summit Quarry For Marble & Granite
Business Card & Full Stationary design For Summit Quarry  - Construction
Creative Brief
Professional
Eng. Karim Haddouri
C.E.O
14 Shari' Nakhil el Wadi, Rawdatein, Giza, 12487, Egypt
kbh@summitquarry.com.eg
www.summitquarry.com.eg
we need everything to be included in the design ( CD, CD Cover, Letterhead, Envelopes, portfolio cover, etc..)
q7rimo q7rimo
I would highly appreciate if you can provide your concepts showing all the required stationaries including the back side of the B.Card ( Letterhead, 2 size envelope, Portfolio cover, CD, CD cover, Backgrounds for smartphones and Computers .)
Vonto Vonto

```html
<!DOCTYPE html>
<html lang="en">
<head>
<meta charset="utf-8">
<title>Summit Quarry — Business Card</title>
<link rel="stylesheet" href="https://fonts.googleapis.com/css2?family=Raleway:wght@300;400;500&display=swap">
<style>
  :root {
    --backdrop: #4f4f4f;
    --card-white: #fbfbf9;
    --card-shade: #e6e6e3;
    --sand: #d3c8ad;
    --sand-light: #e9e3d4;
    --ink: #4a4a4a;
    --ink-soft: #777;
    --logo-tone: #bdae8c;
  }
  * { box-sizing: border-box; margin: 0; padding: 0; }
  html, body { width: 1200px; height: 840px; overflow: hidden; }
  body {
    background: var(--backdrop);
    font-family: "Raleway", "Helvetica Neue", Arial, sans-serif;
    color: var(--ink);
    position: relative;
  }
  .card {
    position: absolute;
    width: 520px;
    height: 300px;
    top: 270px;
    background: linear-gradient(135deg, #ffffff 0%, var(--card-white) 55%, var(--card-shade) 100%);
    box-shadow: 0 6px 18px rgba(0,0,0,.35);
    overflow: hidden;
  }
  .card--front { left: 50px; }
  .card--back { left: 630px; }

  .card__decor { position: absolute; }
  .card--front .card__decor {
    left: 0; top: 0; width: 320px; height: 240px;
    background: linear-gradient(135deg, var(--sand) 0%, var(--sand-light) 45%, rgba(251,251,249,0) 80%);
  }
  .card--back .card__decor {
    right: 0; top: 0; width: 240px; height: 170px;
    background: linear-gradient(225deg, var(--sand-light) 0%, rgba(233,227,212,.5) 45%, rgba(251,251,249,0) 80%);
  }

  .contact {
    position: absolute;
    right: 26px;
    top: 34px;
    text-align: right;
    font-size: 10.5px;
    line-height: 1.45;
  }
  .contact__name { font-size: 17px; font-weight: 500; letter-spacing: 1.5px; }
  .contact__role { font-size: 11px; letter-spacing: 1.5px; color: var(--ink-soft); margin-bottom: 44px; }
  .contact__address { margin-bottom: 18px; }
  .contact__line { display: flex; justify-content: flex-end; align-items: center; gap: 8px; margin-bottom: 6px; }
  .contact__line svg { width: 10px; height: 10px; fill: var(--ink-soft); }

  .wordmark {
    position: absolute;
    font-weight: 300;
    color: var(--logo-tone);
    letter-spacing: 1px;
    white-space: nowrap;
  }
  .card--front .wordmark { left: 32px; bottom: 52px; font-size: 24px; }
  .card--back .wordmark { left: 40px; bottom: 58px; font-size: 30px; }
</style>
</head>
<body>

  <section class="card card--front" aria-label="Business card front">
    <div class="card__decor" role="img" aria-label="Decorative sand-toned wave artwork"></div>

    <div class="contact">
      <p class="contact__name">KARIM HADDOURI</p>
      <p class="contact__role">DIRECTOR</p>
      <p class="contact__address">14 Shari' Nakhil el Wadi<br>Rawdatein, Giza 12487</p>
      <p class="contact__line">012 480 5173
        <svg viewBox="0 0 10 10"><path d="M2 0 L4 2 L3 3.5 C4 5 5 6 6.5 7 L8 6 L10 8 L8.5 10 C4 9 1 6 0 1.5 Z"/></svg></p>
      <p class="contact__line">012 480 5174
        <svg viewBox="0 0 10 10"><path d="M2.5 0 H7.5 V10 H2.5 Z M3.5 1 V8 H6.5 V1 Z"/></svg></p>
      <p class="contact__line">012 480 5175
        <svg viewBox="0 0 10 10"><path d="M2 0 H8 V3 H10 V8 H0 V3 H2 Z M3 1 V3 H7 V1 Z M2 9 H8 V10 H2 Z"/></svg></p>
      <p class="contact__line">kbh@summitquarry.com.eg
        <svg viewBox="0 0 10 10"><path d="M0 2 H10 V8 H0 Z M1 3 L5 6 L9 3 Z"/></svg></p>
      <p class="contact__line">www.summitquarry.com.eg
        <svg viewBox="0 0 10 10"><circle cx="5" cy="5" r="5"/></svg></p>
    </div>

    <p class="wordmark">Summit Quarry</p>
  </section>

  <section class="card card--back" aria-label="Business card back">
    <div class="card__decor" role="img" aria-label="Decorative sand-toned wave artwork"></div>
    <p class="wordmark">Summit Quarry</p>
  </section>

</body>
</html>
```